New Website for World Wide Charity (KELVOR)

We need a dynamic web design for our brand new charity organisation that will be working worldwide. We will be funded by donations so need to attract people to donate.

What We Do
We work to optimise the wellbeing of the planet, the animals and all that live within. Our slogan is Achieving Vibrational Equilibrium.

We have included a Powerpoint document which may help you understand what we need, it is just an idea for structure and style, it is not set in stone so feel free to be as creative as you like!
Updates

Designs look the same

Target Market(s)

Adults 18+ with an interest in animal, environmental. Businesses that may like to support our natural world or already support our natural world.

Number of Pages Required

3 page

Colors

Designer to choose colors to be used in the design.

Requirements
Must have
• We need the website to be easy to use and understand.

Web pages will be Home, What We Do, Who We Are, Success Stories, What You Can Do (Blog section), Seek Help, Donate, Join.
Nice to have
• Natural feel, easy to navigate, Ideally the website will look natural and organic.

Natural colours, blues, greens, sand, gold, brown, grey, silver, Orange and yellow for impact.
Should not have
• Should not have a dark coloured theme.

```html
<!DOCTYPE html>
<html lang="en">
<head>
<meta charset="utf-8">
<title>Kelvor — Help Raise World Vibration</title>
<link href="https://fonts.googleapis.com/css2?family=Poppins:wght@400;500;600;700&family=Oswald:wght@500;600&display=swap" rel="stylesheet">
<style>
:root{
  --blue:#2b4e96;
  --navy:#1f2f6b;
  --ink:#222222;
  --text:#3a3a3a;
  --muted:#8a8394;
  --lav:#e9e1ea;
  --lav-deep:#d9cfe0;
  --lav-panel:#ece7f0;
  --grey-bg:#f6f6f6;
  --white:#ffffff;
  --footer:#ddd6e6;
  --card-label:#d7cbe0;
}
*{margin:0;padding:0;box-sizing:border-box}
html,body{width:1200px;height:3664px;overflow:hidden}
body{position:relative;font-family:"Poppins",sans-serif;color:var(--text);background:var(--white)}
.abs{position:absolute}
a{color:inherit;text-decoration:none}

/* top bar */
.topbar{left:0;top:0;width:1200px;height:71px;background:var(--white)}
.contact-item{top:28px;font-size:12px;color:#555;display:flex;align-items:center;gap:7px}
.socials{top:30px;left:810px;display:flex;gap:12px}
.dot{width:10px;height:10px;border-radius:50%;background:#8d8fa6}
.top-btn{top:24px;height:27px;border:1px solid #9fa8c8;color:var(--blue);font-size:12px;font-weight:600;display:flex;align-items:center;justify-content:center}
.navband{left:0;top:71px;width:1200px;height:43px;background:var(--blue)}
.nav-link{top:86px;color:var(--white);font-size:12px;font-weight:600;letter-spacing:.2px}
.nav-link.active{border-bottom:1px solid var(--white);padding-bottom:2px}
.logo-badge{left:525px;top:16px;width:148px;height:148px;border-radius:50%;background:var(--white);border:6px solid #e4e2ee;display:flex;align-items:center;justify-content:center}
.logo-badge span,.footer-logo span{font-size:19px;font-weight:500;color:var(--blue);letter-spacing:.5px}

/* hero */
.hero{left:0;top:114px;width:1200px;height:651px;background:linear-gradient(180deg,#e9dde6 0%,#ded3de 45%,#c9c2c9 80%,#b8b6b6 100%)}
.hero-title{left:0;top:258px;width:1200px;text-align:center;font-size:44px;font-weight:700;line-height:50px;color:var(--ink)}
.hero-sub{left:0;top:368px;width:1200px;text-align:center;font-size:20px;font-weight:500;color:var(--blue)}
.hero-btn{left:492px;top:418px;width:215px;height:41px;border:2px solid var(--blue);color:var(--blue);font-size:15px;font-weight:500;display:flex;align-items:center;justify-content:center}

.cause-card{top:604px;width:320px;height:253px;background:var(--white);padding:6px;box-shadow:0 2px 8px rgba(0,0,0,.08)}
.cause-card .photo{width:100%;height:100%}
.cause-label{position:absolute;bottom:6px;background:var(--white);font-family:"Oswald",sans-serif;font-weight:500;font-size:23px;color:var(--blue);display:flex;flex-direction:column;align-items:center;justify-content:center}
.cause-label.lit{background:var(--card-label)}
.cause-label small{font-family:"Poppins",sans-serif;font-size:10px;font-weight:500;margin-top:2px}

/* sections */
.side-panel{background:var(--lav-panel)}
.feature-photo{}
.feature-head{font-family:"Oswald",sans-serif;font-weight:600;font-size:28px;color:var(--blue)}
.ghost{font-family:"Oswald",sans-serif;font-weight:600;font-size:40px;color:rgba(43,78,150,.07)}
.feature-copy{width:410px;font-size:13px;line-height:20px;color:var(--text)}
.feature-copy p{margin-bottom:19px}
.read-btn{width:115px;height:32px;border:2px solid var(--blue);color:var(--blue);font-size:11px;font-weight:500;display:flex;align-items:center;justify-content:center;gap:5px}

/* blogs */
.blogs{left:0;top:2684px;width:1200px;height:609px;background:linear-gradient(180deg,#efe6ee 0%,#e6dde7 60%,#d7d2da 100%)}
.blogs-title{left:0;top:2748px;width:1160px;text-align:center;font-family:"Oswald",sans-serif;font-weight:600;font-size:28px;color:var(--blue)}
.blog-photo{border:4px solid var(--white)}
.blog-title-lg{font-size:18px;font-weight:500;line-height:26px;color:var(--ink)}
.blog-title-sm{font-size:13px;font-weight:500;line-height:20px;color:var(--ink)}
.blog-meta{display:flex;align-items:center;gap:6px;font-size:11px;color:var(--blue);font-weight:500}
.blog-btn{height:30px;border:2px solid var(--blue);color:var(--blue);font-size:11px;font-weight:500;display:flex;align-items:center;justify-content:center;gap:4px}

/* footer */
.footer{left:0;top:3293px;width:1200px;height:335px;background:var(--footer)}
.footer-logo{left:108px;top:3362px;width:148px;height:148px;border-radius:50%;background:#efeaf3;border:3px solid var(--blue);display:flex;align-items:center;justify-content:center}
.foot-col h4{font-size:15px;font-weight:500;color:var(--blue);margin-bottom:16px}
.foot-col li{list-style:none;font-size:12px;color:#666;margin-bottom:8px}
.foot-contact{display:flex;gap:10px;font-size:12px;color:#555;margin-bottom:14px;line-height:18px}
.ridge{left:0;top:3540px;width:1200px;height:88px;background:linear-gradient(180deg,rgba(221,214,230,0) 0%,#5a5f8e 55%,#2d3566 100%)}
.bottombar{left:0;top:3628px;width:1200px;height:36px;background:var(--blue);color:var(--white);font-size:12px}
</style>
</head>
<body>

<!-- header -->
<div class="abs topbar"></div>
<div class="abs contact-item" style="left:98px">
  <svg width="12" height="9" viewBox="0 0 12 9"><rect x=".5" y=".5" width="11" height="8" fill="none" stroke="#2b4e96"/><path d="M.5 .5 6 5l5.5-4.5" fill="none" stroke="#2b4e96"/></svg>
  hello@kelvor.org
</div>
<div class="abs contact-item" style="left:270px">
  <svg width="11" height="11" viewBox="0 0 24 24"><path d="M6.6 10.8a15 15 0 0 0 6.6 6.6l2.2-2.2a1 1 0 0 1 1-.25 11.4 11.4 0 0 0 3.6.57 1 1 0 0 1 1 1V20a1 1 0 0 1-1 1A17 17 0 0 1 3 4a1 1 0 0 1 1-1h3.5a1 1 0 0 1 1 1c0 1.25.2 2.45.57 3.57a1 1 0 0 1-.25 1z" fill="#2b4e96"/></svg>
  (555) 014-2290
</div>
<div class="abs socials"><span class="dot"></span><span class="dot"></span><span class="dot"></span><span class="dot"></span></div>
<a class="abs top-btn" style="left:923px;width:93px">DONATE</a>
<a class="abs top-btn" style="left:1031px;width:72px">JOIN</a>

<div class="abs navband"></div>
<a class="abs nav-link active" style="left:98px">HOME</a>
<a class="abs nav-link" style="left:178px">WHAT WE DO</a>
<a class="abs nav-link" style="left:300px">WHO WE ARE</a>
<a class="abs nav-link" style="left:843px">SUCCESS STORIES</a>
<a class="abs nav-link" style="left:989px">WHAT YOU CAN DO</a>
<div class="abs logo-badge"><span>KELVOR</span></div>

<!-- hero -->
<div class="abs hero" role="img" aria-label="Misty pine forest in soft lavender haze"></div>
<h1 class="abs hero-title">HELP RAISE<br>WORLD VIBRATION</h1>
<p class="abs hero-sub">Achieving Vibrational Equilibrium</p>
<a class="abs hero-btn">MAKE A DIFFERENCE</a>

<div class="abs cause-card" style="left:97px">
  <div class="photo" role="img" aria-label="Finger touching a young green seedling" style="background:linear-gradient(135deg,#5c5c5c,#2e2e2e 60%,#6b8f2c)"></div>
  <div class="cause-label" style="left:66px;width:248px;height:56px">ENVIRONMENT</div>
</div>
<div class="abs cause-card" style="left:441px">
  <div class="photo" role="img" aria-label="Child greeting a dog through a fence" style="background:linear-gradient(135deg,#9a9a9a,#555 55%,#b4b4b4)"></div>
  <div class="cause-label" style="left:56px;width:200px;height:56px">ANIMAL</div>
</div>
<div class="abs cause-card" style="left:782px">
  <div class="photo" role="img" aria-label="Volunteers handing out a bowl of soup" style="background:linear-gradient(135deg,#a8a6ab,#6d6f78 50%,#c49a93)"></div>
  <div class="cause-label lit" style="left:58px;width:194px;height:74px">HUMAN<small>FIND OUT MORE →</small></div>
</div>

<!-- environment -->
<div class="abs side-panel" style="left:0;top:931px;width:186px;height:585px"></div>
<div class="abs feature-photo" role="img" aria-label="Finger touching a young green seedling in dark soil" style="left:98px;top:1021px;width:501px;height:398px;background:linear-gradient(135deg,#6a6a6a,#2b2b2b 55%,#5f8a23 75%,#232323)"></div>
<div class="abs ghost" style="left:673px;top:1050px">ENVIRONMENT</div>
<h2 class="abs feature-head" style="left:673px;top:1066px">ENVIRONMENT</h2>
<div class="abs feature-copy" style="left:674px;top:1136px">
  <p>Lorem Ipsum is simply dummy text of the printing and typeset-ting industry.</p>
  <p>Lorem Ipsum has been the industry's standard dummy text ever since the 1500s, when an unknown printer took a galley of type and scrambled it to make a type specimen book.</p>
  <p>It has survived not only five centuries, but also the leap into electronic typesetting, remaining essentially unchanged.</p>
</div>
<a class="abs read-btn" style="left:674px;top:1354px">Read More <span>→</span></a>

<!-- animal -->
<div class="abs" style="left:0;top:1516px;width:1200px;height:584px;background:var(--grey-bg)"></div>
<div class="abs side-panel" style="left:1012px;top:1516px;width:188px;height:584px"></div>
<div class="abs ghost" style="left:97px;top:1640px">ANIMAL</div>
<h2 class="abs feature-head" style="left:97px;top:1656px">ANIMAL</h2>
<div class="abs feature-copy" style="left:99px;top:1721px">
  <p>Lorem Ipsum is simply dummy text of the printing and typeset-ting industry.</p>
  <p>Lorem Ipsum has been the industry's standard dummy text ever since the 1500s, when an unknown printer took a galley of type and scrambled it to make a type specimen book.</p>
  <p>It has survived not only five centuries, but also the leap into electronic typesetting, remaining essentially unchanged.</p>
</div>
<a class="abs read-btn" style="left:98px;top:1938px">Read More <span>→</span></a>
<div class="abs feature-photo" role="img" aria-label="Child pressing her head to a dog through a wooden fence" style="left:600px;top:1607px;width:501px;height:398px;background:linear-gradient(135deg,#a5a5a5,#5a5a5a 50%,#c0c0c0)"></div>

<!-- human -->
<div class="abs side-panel" style="left:0;top:2100px;width:186px;height:584px"></div>
<div class="abs feature-photo" role="img" aria-label="Masked volunteers handing a bowl of soup to someone in need" style="left:98px;top:2191px;width:501px;height:398px;background:linear-gradient(135deg,#b2aeb2,#7b7c86 45%,#c89d95 75%,#7c6a58)"></div>
<div class="abs ghost" style="left:673px;top:2220px">HUMAN</div>
<h2 class="abs feature-head" style="left:673px;top:2236px">HUMAN</h2>
<div class="abs feature-copy" style="left:674px;top:2306px">
  <p>Lorem Ipsum is simply dummy text of the printing and typeset-ting industry.</p>
  <p>Lorem Ipsum has been the industry's standard dummy text ever since the 1500s, when an unknown printer took a galley of type and scrambled it to make a type specimen book.</p>
  <p>It has survived not only five centuries, but also the leap into electronic typesetting, remaining essentially unchanged.</p>
</div>
<a class="abs read-btn" style="left:674px;top:2522px">Read More <span>→</span></a>

<!-- blogs -->
<div class="abs blogs"></div>
<div class="abs ghost" style="left:0;top:2736px;width:1230px;text-align:center">BLOGS</div>
<h2 class="abs blogs-title">BLOGS</h2>

<div class="abs blog-photo" role="img" aria-label="Volunteer collecting plastic bottles from the grass" style="left:98px;top:2834px;width:489px;height:256px;background:linear-gradient(135deg,#7cba3a,#3c3f44 50%,#3d8fe0 75%,#6fb132)"></div>
<a class="abs" style="left:645px;top:2855px;font-size:10px;color:var(--blue);font-weight:500">View All →</a>
<h3 class="abs blog-title-lg" style="left:645px;top:2877px;width:300px">Good vibes or bad vibes Which do you prefer?</h3>
<p class="abs" style="left:645px;top:2942px;width:440px;font-size:12px;line-height:21px;color:var(--muted)">Lorem Ipsum is simply dummy text of the printing and typesetting in-dustry. Lorem Ipsum has been the industry's standard...</p>
<div class="abs blog-meta" style="left:646px;top:3021px">
  <svg width="14" height="14" viewBox="0 0 14 14"><rect x="1" y="2.5" width="12" height="10.5" fill="none" stroke="#2b4e96" stroke-width="1.4"/><path d="M1 5.5h12M4 1v3M10 1v3" stroke="#2b4e96" stroke-width="1.4"/></svg>08 Feb 2021
</div>
<a class="abs blog-btn" style="left:768px;top:3013px;width:114px">Read More <span>→</span></a>

<div class="abs blog-photo" role="img" aria-label="Glass globe resting on mossy ground" style="left:98px;top:3112px;width:182px;height:97px;background:linear-gradient(135deg,#2d2a10,#8c8a2a 55%,#c9b552)"></div>
<h3 class="abs blog-title-sm" style="left:303px;top:3122px;width:200px">Lorem Ipsum is simply dummy text of the printing...</h3>
<div class="abs blog-meta" style="left:304px;top:3178px">
  <svg width="13" height="13" viewBox="0 0 14 14"><rect x="1" y="2.5" width="12" height="10.5" fill="none" stroke="#2b4e96" stroke-width="1.4"/><path d="M1 5.5h12M4 1v3M10 1v3" stroke="#2b4e96" stroke-width="1.4"/></svg>08 Feb 2021
</div>
<a class="abs blog-btn" style="left:413px;top:3171px;width:100px">Read More <span>→</span></a>

<div class="abs blog-photo" role="img" aria-label="Hands protecting a chain of paper figures" style="left:611px;top:3112px;width:182px;height:97px;background:linear-gradient(135deg,#e9d8c4,#d6a18a 50%,#b96a5b)"></div>
<h3 class="abs blog-title-sm" style="left:816px;top:3122px;width:200px">Lorem Ipsum is simply dummy text of the printing...</h3>
<div class="abs blog-meta" style="left:817px;top:3178px">
  <svg width="13" height="13" viewBox="0 0 14 14"><rect x="1" y="2.5" width="12" height="10.5" fill="none" stroke="#2b4e96" stroke-width="1.4"/><path d="M1 5.5h12M4 1v3M10 1v3" stroke="#2b4e96" stroke-width="1.4"/></svg>08 Feb 2021
</div>
<a class="abs blog-btn" style="left:926px;top:3171px;width:100px">Read More <span>→</span></a>

<!-- footer -->
<div class="abs footer"></div>
<div class="abs footer-logo"><span>KELVOR</span></div>
<div class="abs foot-col" style="left:340px;top:3358px">
  <h4>Quick Links</h4>
  <ul><li>Home</li><li>What We Do</li><li>Who We Are</li><li>Success Stories</li><li>What You Can Do</li></ul>
</div>
<div class="abs foot-col" style="left:543px;top:3358px">
  <h4>Get Involved</h4>
  <ul><li>Join Us</li><li>Fundraise</li><li>Donate</li><li>Shop</li></ul>
</div>
<div class="abs foot-col" style="left:738px;top:3358px">
  <h4>Legal</h4>
  <ul><li>Terms and Conditions</li><li>Cookies</li><li>Privacy Policy</li></ul>
</div>
<div class="abs foot-col" style="left:931px;top:3358px">
  <h4>Conatct info</h4>
  <div class="foot-contact"><svg width="12" height="12" viewBox="0 0 24 24"><path d="M6.6 10.8a15 15 0 0 0 6.6 6.6l2.2-2.2a1 1 0 0 1 1-.25 11.4 11.4 0 0 0 3.6.57 1 1 0 0 1 1 1V20a1 1 0 0 1-1 1A17 17 0 0 1 3 4a1 1 0 0 1 1-1h3.5a1 1 0 0 1 1 1c0 1.25.2 2.45.57 3.57a1 1 0 0 1-.25 1z" fill="#444"/></svg>(555) 014-2290</div>
  <div class="foot-contact"><svg width="12" height="10" viewBox="0 0 12 9"><rect x=".5" y=".5" width="11" height="8" fill="#444"/><path d="M.5 .5 6 5l5.5-4.5" fill="none" stroke="#ddd6e6"/></svg>hello@kelvor.org</div>
  <div class="foot-contact"><svg width="12" height="16" viewBox="0 0 12 16"><path d="M6 0a6 6 0 0 0-6 6c0 4.5 6 10 6 10s6-5.5 6-10a6 6 0 0 0-6-6zm0 8.5A2.5 2.5 0 1 1 6 3.5a2.5 2.5 0 0 1 0 5z" fill="#444"/></svg>42 Meadow Lane<br>Fernvale, OR 97010</div>
</div>
<div class="abs ridge" role="img" aria-label="Silhouette of a forested mountain ridge"></div>
<div class="abs bottombar">
  <span class="abs" style="left:98px;top:10px">Copyright © 2021 Kelvor. All Rights Reserved</span>
  <div class="abs" style="left:1010px;top:13px;display:flex;gap:14px"><span class="dot" style="background:#fff"></span><span class="dot" style="background:#fff"></span><span class="dot" style="background:#fff"></span><span class="dot" style="background:#fff"></span></div>
</div>

</body>
</html>
```